lantern pathway for children needs a website designer

We need a website designer for our new extension to our company known as 'lantern pathway' providing shadow support services to children based in Singapore. We are a sister branch of a private clinic 'Bright horizon' providing speech language, occupational, and educational therapy to children.

We would like to use our own photos. So the selected design should have a frame with pictures to give us an idea but we will replace them with our own. We will be needing help with inputting information and changing information throughout.

We would like to see designs that are simple, and professional. We have a logo (see attached). The result should convey professionalism in shadow support, fostering independent thinking and moving students towards self-learning.

Target Market(s)

Teachers, psychologists, parents

Industry/Entity Type

Clinic

Requirements
Should not have
• too distracting colours

```html
<!DOCTYPE html>
<html lang="en">
<head>
<meta charset="utf-8">
<title>Lantern Pathway</title>
<link rel="stylesheet" href="https://fonts.googleapis.com/css2?family=Arimo:wght@400;700&family=Open+Sans:wght@400;600&display=swap">
<style>
:root{
  --red:#8c0d12;
  --red-dark:#6a070b;
  --text:#555;
  --text-soft:#6d6d6d;
  --heading:#333;
  --gold:#d9a516;
  --bar:#3a3a3a;
}
*{margin:0;padding:0;box-sizing:border-box}
html,body{width:1200px;height:2560px;overflow:hidden}
body{position:relative;background:linear-gradient(#f4f4f4,#e9e9e9 900px);font-family:Arimo,Arial,sans-serif;color:var(--text)}
.abs{position:absolute}
.top-line{left:0;top:0;width:1200px;height:8px;background:var(--red-dark)}

/* header */
.nav-bar{left:43px;top:51px;width:1102px;height:48px;border-radius:5px;background:linear-gradient(#a5161c,var(--red-dark));box-shadow:0 2px 4px rgba(0,0,0,.25)}
.nav-bar a{position:absolute;top:16px;color:#fff;font-size:15px;letter-spacing:1px;text-decoration:none;white-space:nowrap}
.brand{left:56px;top:32px;width:204px;height:89px;border-radius:4px;background:linear-gradient(#fff,#dedede);box-shadow:0 2px 5px rgba(0,0,0,.35);display:flex;align-items:center;justify-content:center;font-size:23px;font-weight:700;color:var(--red);white-space:nowrap}

/* hero */
.hero{left:46px;top:145px;width:1108px;height:384px;border-radius:6px;background:linear-gradient(100deg,#eee,#dcdcdc);border:5px solid #d6d6d6;box-shadow:0 2px 6px rgba(0,0,0,.15);overflow:hidden}
.hero-photo{left:0;top:0}
.hero-title{left:499px;top:70px;font-weight:400;font-size:22px;letter-spacing:2.5px;color:var(--heading);white-space:nowrap}
.hero-title span,.welcome span,.card-title span{color:var(--red)}
.hero-text{left:499px;top:106px;width:540px;font-size:16px;line-height:31px;letter-spacing:1.1px;color:var(--text-soft);text-align:justify;hyphens:auto}
.hero-btn{left:504px;top:231px;width:273px;height:47px;background:linear-gradient(#a8161c,var(--red-dark));color:#fff;font-size:21px;letter-spacing:1.5px;display:flex;align-items:center;justify-content:center}
.dots{left:969px;top:350px;display:flex;gap:4px}
.dots i{width:13px;height:13px;border-radius:50%;background:var(--red);border:2px solid #fff}

/* welcome */
.welcome{left:0;top:558px;width:1200px;text-align:center;font-weight:400;font-size:29px;letter-spacing:2px;color:var(--heading)}
.rule{left:154px;top:623px;width:947px;height:1px;background:#c9c9c9}
.intro{left:154px;top:646px;width:875px;text-align:center;font-size:15px;line-height:23px;letter-spacing:1.3px;color:var(--text-soft);hyphens:auto}
.intro p+p{margin-top:21px}

/* services */
.band{left:0;top:900px;width:1200px;height:554px;background:#e3e3e3;background-image:radial-gradient(#d4d4d4 1px,transparent 1px);background-size:4px 4px}
.card{top:913px;width:277px;height:418px;border-radius:8px;background:linear-gradient(#ececec,#c7c7c7);border:6px solid #d8d8d8;box-shadow:0 1px 3px rgba(0,0,0,.2)}
.card-photo{left:50%;top:-105px;width:212px;height:212px;margin-left:-106px;border-radius:50%;border:12px solid #f1f1f1;box-shadow:0 0 0 2px #ddd}
.card-title{left:20px;top:152px;font-weight:400;font-size:22px;letter-spacing:1px;color:var(--heading);white-space:nowrap}
.card-desc{left:20px;top:185px;width:215px;font-size:14px;letter-spacing:.8px;color:var(--text-soft)}
.card-desc ul{list-style:none;margin-top:4px}
.card-desc li{position:relative;padding-left:14px;line-height:17px;margin-bottom:5px;font-size:13.5px}
.card-desc li::before{content:"";position:absolute;left:0;top:4px;width:8px;height:8px;border-radius:50%;background:var(--red)}
.card-btn{left:20px;top:325px;width:220px;height:40px;background:linear-gradient(#a8161c,var(--red-dark));color:#fff;font-size:16px;letter-spacing:1.2px;display:flex;align-items:center;justify-content:center}

/* shadow support */
.support{left:0;top:1454px;width:1200px;height:381px;background:linear-gradient(90deg,#9a1a1e,#a8282c 50%,#951418)}
.support h2{position:absolute;left:0;top:28px;width:1200px;text-align:center;font-weight:400;font-size:26px;letter-spacing:1.5px;color:#fff}
.support .line{position:absolute;left:162px;width:913px;height:1px;background:rgba(255,255,255,.25)}
.support p,.support li{font-family:"Open Sans",Arial,sans-serif;color:#fbeaea;font-size:15px;line-height:24px}
.support-left{left:162px;top:106px;width:422px;text-align:justify}
.support-list{left:645px;top:106px;width:440px;list-style:none}
.support-list li{position:relative;padding-left:20px;margin-bottom:18px;line-height:20px}
.support-list svg{position:absolute;left:0;top:5px}
.support-goal{left:162px;top:279px;width:940px}

/* faq */
.faq{font-family:"Open Sans",Arial,sans-serif}
.faq h3{font-weight:400;font-size:20px;color:var(--red);margin-bottom:16px}
.faq p{font-size:14.5px;line-height:24.5px;color:var(--text-soft);hyphens:auto}
.faq p+p{margin-top:24px}
.faq-left{left:162px;top:1873px;width:435px}
.faq-left h3.second{margin-top:22px}
.faq-right{left:669px;top:1873px;width:435px}
.faq-right p{text-align:justify}
.learn-btn{left:951px;top:2059px;width:153px;height:32px;background:linear-gradient(#a8161c,var(--red-dark));color:#fff;font-size:12px;letter-spacing:1px;display:flex;align-items:center;justify-content:center}

/* footer */
.footer{left:0;top:2292px;width:1200px;height:234px;background:linear-gradient(#9e181d,#850d12)}
.footer h4{position:absolute;top:42px;font-weight:400;font-size:20px;letter-spacing:1px;color:#fff;white-space:nowrap}
.footer .dotted{position:absolute;left:80px;top:79px;width:1012px;border-top:2px dotted #f0c9c9}
.footer ul{position:absolute;top:100px;list-style:none}
.footer li{position:relative;padding-left:10px;color:#fff;font-size:11px;letter-spacing:.6px;line-height:20px}
.footer li::before{content:"";position:absolute;left:0;top:8px;width:5px;height:5px;border-radius:50%;background:#fff}
.social{position:absolute;left:622px;top:109px;display:flex;gap:6px}
.social i{width:33px;height:33px;border-radius:50%;background:#fff}
.email{position:absolute;left:883px;top:105px;width:175px;height:37px;background:#fff;border-radius:3px;font-size:17px;color:#c5c5c5;padding:8px 12px}
.subscribe{position:absolute;left:883px;top:154px;width:175px;height:40px;border-radius:3px;background:linear-gradient(#e6b420,#c9940f);color:#fff;font-size:13px;letter-spacing:1px;display:flex;align-items:center;justify-content:center}
.copyright{left:0;top:2526px;width:1200px;height:34px;background:var(--bar);color:#ddd;font-size:13px;letter-spacing:.5px;display:flex;align-items:center;justify-content:center}
</style>
</head>
<body>
<div class="abs top-line"></div>

<header>
  <nav class="abs nav-bar">
    <a style="left:482px">HOME</a>
    <a style="left:585px">ABOUT US</a>
    <a style="left:716px">SERVICES</a>
    <a style="left:846px">CAREERS</a>
    <a style="left:973px">CONTACT US</a>
  </nav>
  <div class="abs brand">Lantern Pathway</div>
</header>

<section class="abs hero">
  <svg class="abs hero-photo" width="480" height="374" viewBox="0 0 480 374" role="img" aria-label="Photo of a teacher reading with a young pupil in a library">
    <defs><linearGradient id="heroFill" x1="0" y1="0" x2="1" y2="1"><stop offset="0" stop-color="#c9a77d"/><stop offset=".5" stop-color="#b88e5d"/><stop offset="1" stop-color="#e9e4dc"/></linearGradient></defs>
    <path d="M0 0H440C500 120 495 260 440 374H0Z" fill="url(#heroFill)"/>
    <path d="M440 0C500 120 495 260 440 374" fill="none" stroke="#7d0a0f" stroke-width="5"/>
  </svg>
  <h1 class="abs hero-title">SAMPLE TEXT <span>FOR HEADLINE ONLY</span></h1>
  <p class="abs hero-text">Lorem ipsum dolor sit amet, consectetur adipiscing elit. Curabitur lacinia pretium risus ac euismod. Aliquam auctor convallis mattis. lacinia pretium risus ac euismod. Aliquam auctor convallis mattis.</p>
  <div class="abs hero-btn">MAKE AN ENQUIRY</div>
  <div class="abs dots"><i></i><i></i><i></i><i></i></div>
</section>

<h2 class="abs welcome"><span>WELCOME TO</span> LANTERN PATHWAY</h2>
<div class="abs rule"></div>
<div class="abs intro">
  <p>Lantern Pathway is part of the Clearwater Speech Group of Companies, who are providing speech language therapy, occupational therapy and educational therapy services to both the Singapore and the international school community.</p>
  <p>Lantern Pathway aims to work in an integrated manner, respecting the work of the respective professionals involved and collaborating effectively.</p>
</div>

<div class="abs band"></div>

<article class="abs card" style="left:113px">
  <div class="abs card-photo" role="img" aria-label="Photo of a clinician working with a child at a desk" style="background:linear-gradient(135deg,#f4f4f4,#c9d6e3 60%,#e3b58a)"></div>
  <h3 class="abs card-title"><span>For</span> Referrers</h3>
  <div class="abs card-desc">Short description goes here.
    <ul><li>How You Can Collaborate With Us</li></ul></div>
  <div class="abs card-btn">READ MORE</div>
</article>

<article class="abs card" style="left:464px">
  <div class="abs card-photo" role="img" aria-label="Photo of children sitting on a colourful classroom rug" style="background:linear-gradient(135deg,#3f5a8a,#c9a23a 50%,#8a3b2a)"></div>
  <h3 class="abs card-title"><span>For</span> Parents</h3>
  <div class="abs card-desc">Short description goes here.
    <ul><li>Registration Form</li><li>Cost Estimation</li></ul></div>
  <div class="abs card-btn">READ MORE</div>
</article>

<article class="abs card" style="left:816px">
  <div class="abs card-photo" role="img" aria-label="Photo of the school team standing together" style="background:linear-gradient(#6d6a66,#3a3a3a 60%,#8a8580)"></div>
  <h3 class="abs card-title"><span>For</span> Schools</h3>
  <div class="abs card-desc">Short description goes here'
    <ul><li>How do we help you achieve your goals</li><li>How do I know if my child needs support</li><li>School Terms</li></ul></div>
  <div class="abs card-btn">READ MORE</div>
</article>

<section class="abs support">
  <h2>WHAT IS SHADOW SUPPORT?</h2>
  <div class="line" style="top:74px"></div>
  <p class="abs support-left">A shadow support is para-professional who can help a struggling student to integrate and learn in their school environment. At different points in a student's life, there may be a need for a para-professional who could step in to help make a difference. Students who need shadows are those who:</p>
  <ul class="abs support-list">
    <li><svg width="12" height="10" viewBox="0 0 12 10"><path d="M0 5H10M6 1L10 5L6 9" fill="none" stroke="#fff" stroke-width="1.6"/></svg>Have difficulties in integrating learning in classroom</li>
    <li><svg width="12" height="10" viewBox="0 0 12 10"><path d="M0 5H10M6 1L10 5L6 9" fill="none" stroke="#fff" stroke-width="1.6"/></svg>Have social challenges and find it difficult to connect with peers</li>
    <li><svg width="12" height="10" viewBox="0 0 12 10"><path d="M0 5H10M6 1L10 5L6 9" fill="none" stroke="#fff" stroke-width="1.6"/></svg>Have difficulties in understanding instructions</li>
  </ul>
  <p class="abs support-goal">A central goal of the shadow support would be to help the student achieve independence in their learning journey eventually.</p>
  <div class="line" style="top:347px;left:480px;width:380px"></div>
</section>

<section class="abs faq faq-left">
  <h3>What are its Advantages?</h3>
  <p>A fully trained shadow support is an asset to the student who otherwise would have trouble fitting in and adapting to the mainstream school environment.</p>
  <p>Additionally, working closely with the therapist at the centre would mean that the shadow is equipped with the skills necessary to not just adapt, but truly learn.</p>
  <h3 class="second">How do I know if my child needs shadowing</h3>
  <p>A consultation with our Speech Language Pathologist, along with an assessment by an Educational Psychologist would provide us with an indication of whether the child requires shadowing.</p>
</section>

<section class="abs faq faq-right">
  <h3>Will this create a crutch mentality?</h3>
  <p>A great shadow possesses great dynamic skills that allow her to know when to step back and when to jump in. Focus is on building skills at every opportune moment, including classrooms and during breaks. Focus is also on building independence so that the shadow can be weaned off at the right moment.</p>
</section>
<div class="abs learn-btn">LEARN MORE</div>

<footer class="abs footer">
  <h4 style="left:114px">Navigation</h4>
  <h4 style="left:329px">Useful Information</h4>
  <h4 style="left:620px">Interact with us</h4>
  <h4 style="left:881px">Newsletter</h4>
  <div class="dotted"></div>
  <ul style="left:122px"><li>HOME</li><li>ABOUT US</li><li>SERVICES</li><li>NEWS</li><li>REGISTER</li><li>CONTACT US</li></ul>
  <ul style="left:337px;top:96px"><li>Sitemap</li><li>FAQ</li><li>Terms &amp; Conditions</li><li>Privacy Policy</li></ul>
  <div class="social"><i></i><i></i><i></i><i></i></div>
  <div class="email">your email</div>
  <div class="subscribe">SUBSCRIBE</div>
</footer>
<div class="abs copyright">Copyright 2013 · All rights reserved</div>
</body>
</html>
```